Protrait photographers business card

Need a new catchy, chic business card to promote my new portrait photograghy business. Love taking the natural, location portraits of families, children, teens. It should look classy, but also warm & friendly. I want it to show that Famliy, friends, couples & childten are what I love photographing, so if it can have that sort of feel to it & also looking energetic.

Target Market(s)

Families, couples, babies, people on holidays wanting some locational professional photos

Industry/Entity Type

Portrait Photography

Contact Information for Business Card

Marisol photography, By Tavi, Lorna Brackwell,Ph: 0437586204, Pelican reach, Qld

Font styles to use
Decorative
Script

Requirements
Must have
• Company name & photographers name
Nice to have
• a coloured card
Should not have
• not be on a white card

```html
<!DOCTYPE html>
<html lang="en">
<head>
<meta charset="utf-8">
<title>Marisol photography – business card</title>
<link rel="stylesheet" href="https://fonts.googleapis.com/css2?family=Dancing+Script:wght@400;500&family=Great+Vibes&display=swap">
<style>
  :root{
    --pink:#d6186b;
    --purple:#8c47a0;
    --ink:#000000;
    --page:#ffffff;
    --photo-frame:#ffffff;
  }
  *{margin:0;padding:0;box-sizing:border-box}
  html,body{width:1035px;height:1200px;overflow:hidden;background:var(--page)}
  .canvas{position:relative;width:1035px;height:1200px}
  .card{
    position:absolute;left:70px;width:898px;height:554px;
    background:var(--ink);overflow:hidden;
    box-shadow:0 4px 10px rgba(0,0,0,.35);
  }
  .card--front{top:31px;
    background:radial-gradient(circle at 416px 212px,#2a2a2a 0,#121212 150px,var(--ink) 320px);}
  .card--back{top:614px}
  .band{position:absolute;inset:0;width:898px;height:554px}
  .photo{
    position:absolute;border:4px solid var(--photo-frame);
    box-shadow:0 3px 8px rgba(0,0,0,.6);
  }
  .photo--family{left:57px;top:86px;width:186px;height:154px;transform:rotate(-17deg);
    background:linear-gradient(135deg,#c9584e,#5d7a9e 55%,#2f3a4a)}
  .photo--child{left:253px;top:97px;width:182px;height:146px;transform:rotate(-4deg);
    background:linear-gradient(160deg,#6f8a3b,#3e5b2a 60%,#2b3b5e)}
  .photo--portrait{left:126px;top:234px;width:194px;height:150px;transform:rotate(3deg);
    background:radial-gradient(circle at 50% 45%,#c99a7c 0,#e7e2de 45%,#f6f6f6 80%)}
  .photo--couple{left:345px;top:214px;width:206px;height:158px;transform:rotate(-14deg);
    background:linear-gradient(180deg,#e4ddc0,#9b9478 55%,#4a473c)}
  .brand-mark{position:absolute;left:600px;top:370px;display:flex;align-items:center;gap:14px}
  .brand-mark__dot{width:34px;height:34px;border-radius:50%;background:var(--purple)}
  .brand-mark__name{font-family:"Dancing Script",cursive;font-size:46px;color:var(--pink);line-height:1}
  .back-circle{position:absolute;left:-160px;top:60px;width:420px;height:420px;border-radius:50%;background:#161616}
  .text{position:absolute;white-space:nowrap;line-height:1}
  .company{right:106px;top:46px;font-family:"Dancing Script",cursive;font-weight:500;font-size:90px;color:var(--pink)}
  .company-sub{right:41px;top:143px;font-family:"Dancing Script",cursive;font-size:48px;letter-spacing:4px;color:var(--pink)}
  .byline{right:47px;top:215px;font-family:"Dancing Script",cursive;font-size:24px;color:var(--purple)}
  .centered{left:0;width:898px;text-align:center}
  .person{top:232px;padding-left:0;font-family:"Great Vibes",cursive;font-size:60px;color:var(--pink);letter-spacing:1px}
  .email{top:318px;font-family:"Dancing Script",cursive;font-size:28px;letter-spacing:3px;color:var(--purple)}
  .phone{top:384px;font-family:"Dancing Script",cursive;font-size:38px;letter-spacing:4px;color:var(--purple)}
  .place{top:444px;font-family:"Dancing Script",cursive;font-size:32px;letter-spacing:3px;color:var(--purple)}
</style>
</head>
<body>
<div class="canvas">
  <section class="card card--front">
    <svg class="band" viewBox="0 0 898 554" aria-hidden="true">
      <polygon points="489,0 898,0 898,57 525,57" fill="var(--purple)"/>
      <polygon points="0,497 374,497 409,554 0,554" fill="var(--pink)"/>
    </svg>
    <div class="photo photo--family" role="img" aria-label="Photo of a father smiling with his young son outdoors"></div>
    <div class="photo photo--child" role="img" aria-label="Photo of a toddler in a cap walking through a garden"></div>
    <div class="photo photo--portrait" role="img" aria-label="Studio portrait of a smiling teenage girl"></div>
    <div class="photo photo--couple" role="img" aria-label="Sepia photo of a couple with a guitar beside a palm tree"></div>
    <div class="brand-mark">
      <span class="brand-mark__dot"></span>
      <span class="brand-mark__name">Marisol</span>
    </div>
  </section>

  <section class="card card--back">
    <div class="back-circle" aria-hidden="true"></div>
    <svg class="band" viewBox="0 0 898 554" aria-hidden="true">
      <polygon points="0,0 409,0 372,57 0,57" fill="var(--purple)"/>
      <polygon points="525,497 898,497 898,554 489,554" fill="var(--pink)"/>
    </svg>
    <h1 class="text company">Marisol</h1>
    <p class="text company-sub">photography</p>
    <p class="text byline">By Tavi</p>
    <p class="text centered person">Lorna Brackwell</p>
    <p class="text centered email">marisolphotography@outlook.com</p>
    <p class="text centered phone">Ph: 0437 586 204</p>
    <p class="text centered place">Pelican Reach QLD</p>
  </section>
</div>
</body>
</html>
```